Golden Pantry Spice

Distributor of seasonings and spices to the restaurant industry.

Industry/Entity Type

Restaurant

Contact Information for Business Card

Golden Pantry
Derek Hollings
TW Brandvik Distributor
316-487-9021
derek@goldpantryspicehub.com

No minimum order
Gluten & MSG free soup bases

```html
<!DOCTYPE html>
<html lang="en">
<head>
<meta charset="utf-8">
<title>Golden Pantry Spice – Business Card</title>
<link rel="stylesheet" href="https://fonts.googleapis.com/css2?family=Josefin+Sans:wght@300;400&display=swap">
<style>
  :root {
    --page-bg: #e9e7e4;
    --card-orange: #f26a21;
    --ink-brown: #6a3524;
    --rule-brown: #7a3d27;
  }
  * { margin: 0; padding: 0; box-sizing: border-box; }
  html, body {
    width: 1200px;
    height: 1023px;
    overflow: hidden;
    background: var(--page-bg);
  }
  .stage {
    position: relative;
    width: 1200px;
    height: 1023px;
  }
  .business-card {
    position: absolute;
    left: 180px;
    top: 271px;
    width: 840px;
    height: 480px;
    background: var(--card-orange);
    box-shadow: 0 10px 30px rgba(0,0,0,0.18);
    font-family: "Josefin Sans", "Century Gothic", sans-serif;
    font-weight: 300;
    color: var(--ink-brown);
  }
  .rule {
    position: absolute;
    height: 1.5px;
    background: var(--rule-brown);
  }
  .rule--top     { left: 60px;  top: 120px; width: 720px; }
  .rule--name    { left: 350px; top: 198px; width: 410px; }
  .rule--contact { left: 350px; top: 282px; width: 390px; }
  .rule--bottom  { left: 60px;  top: 362px; width: 660px; }
  .divider {
    position: absolute;
    left: 330px;
    top: 140px;
    width: 1.5px;
    height: 205px;
    background: var(--rule-brown);
  }
  .brand-name {
    position: absolute;
    left: 60px;
    top: 218px;
    font-size: 36px;
    letter-spacing: 0.5px;
    white-space: nowrap;
  }
  .brand-role {
    position: absolute;
    left: 62px;
    top: 318px;
    font-size: 18px;
    letter-spacing: 0.5px;
    white-space: nowrap;
  }
  .person-name {
    position: absolute;
    left: 352px;
    top: 138px;
    font-size: 46px;
    letter-spacing: 1px;
    white-space: nowrap;
  }
  .contact-list, .service-list {
    position: absolute;
    left: 352px;
    list-style: none;
    font-size: 19px;
    line-height: 30px;
    letter-spacing: 0.5px;
    white-space: nowrap;
  }
  .contact-list { top: 212px; }
  .service-list { top: 294px; }
</style>
</head>
<body>
<main class="stage">
  <article class="business-card">
    <div class="rule rule--top"></div>
    <div class="rule rule--name"></div>
    <div class="rule rule--contact"></div>
    <div class="rule rule--bottom"></div>
    <div class="divider"></div>

    <p class="brand-name">Golden Pantry</p>
    <p class="brand-role">TW Brandvik Distributor</p>

    <h1 class="person-name" style="font-weight:300">Derek Hollings</h1>
    <ul class="contact-list">
      <li>316-487-9021</li>
      <li>derek@goldpantryspicehub.com</li>
    </ul>
    <ul class="service-list">
      <li>No minimum order</li>
      <li>Gluten &amp; MSG free soup bases</li>
    </ul>
  </article>
</main>
</body>
</html>
```